Business Card Design

Im electrician in melbourne after a business cards. I have no logos done. I have attached a card that i like but needs to be altered to my business name, so in the picture shows a lead plug into a socket spelling plug, i want the spelling replaced with my company name. I was thinking some thing with a charcoal back ground with yellow or green font.
I have wrote what I'd like above but feel free to try your own ideas and designs.
Industry/Entity Type
Electrician
Contact Information for Business Card
Vorn Electrical Services PTY LTD (Display on the front of card, the PTY LTD can be in small font)
REC:58104 (also on the front in small font)
Call Teodor (back i dont want my last name on the card)
Phone: 0488157093 (back
Email: vornelectricalservices@kestramail.com (back)
Domestic, Commercial, Industrial, (on the back in dot points.)
Look and feel
Each slider illustrates characteristics of the customer's brand and the style your logo design should communicate.

```html
<!DOCTYPE html>
<html lang="en">
<head>
<meta charset="utf-8">
<title>Vorn Electrical Services – Business Card</title>
<link href="https://fonts.googleapis.com/css2?family=Open+Sans:wght@400;600;700&display=swap" rel="stylesheet">
<style>
  :root {
    --backdrop: #b3b3b3;
    --charcoal: #3a3a3b;
    --brand-accent: #a6d13a;
    --band-accent: #8dbf2e;
    --panel-top: #96c935;
    --panel-bottom: #7aad25;
    --icon-light: #9acb3a;
    --icon-mid: #6a9a20;
    --icon-dark: #4a7014;
    --name-box: #8c8c8c;
    --text-light: #ffffff;
    --text-muted: #ececec;
    --text-on-accent: #1f2a0e;
  }
  * { box-sizing: border-box; margin: 0; padding: 0; }
  html, body { width: 1200px; height: 894px; overflow: hidden; }
  body { background: var(--backdrop); font-family: "Open Sans", Arial, sans-serif; }
  .canvas { position: relative; width: 1200px; height: 894px; overflow: hidden; background: var(--backdrop); }

  .card {
    position: absolute; width: 560px; height: 320px;
    background: var(--charcoal); overflow: hidden;
    box-shadow: 0 6px 18px rgba(0,0,0,0.25);
  }
  .card--front { left: 560px; top: 110px; }
  .card--back { left: 80px; top: 450px; }

  /* Front */
  .band { position: absolute; left: 0; right: 0; height: 34px; background: var(--band-accent); }
  .band--top { top: 0; }
  .band--bottom { bottom: 0; }
  .brand { position: absolute; color: var(--brand-accent); font-weight: 700; line-height: 1; }
  .brand__name { display: block; text-transform: uppercase; letter-spacing: 1px; }
  .brand__suffix { display: block; text-transform: uppercase; letter-spacing: 6px; }
  .card--front .brand { left: 80px; top: 116px; }
  .card--front .brand__name { font-size: 36px; }
  .card--front .brand__suffix { font-size: 16px; margin-top: 6px; }
  .licence {
    position: absolute; left: 80px; top: 206px;
    color: var(--text-muted); font-size: 11px; letter-spacing: 2px;
  }

  /* Back */
  .card--back .brand { left: 70px; top: 38px; }
  .card--back .brand__name { font-size: 28px; }
  .card--back .brand__suffix { font-size: 12px; margin-top: 5px; letter-spacing: 5px; }

  .name-box {
    position: absolute; left: 56px; top: 105px; width: 206px; height: 128px;
    background: var(--name-box); padding: 24px 18px; color: var(--text-light);
  }
  .name-box__name { font-size: 17px; font-weight: 400; letter-spacing: 0.5px; text-transform: uppercase; }
  .name-box__title { font-size: 10px; color: var(--text-muted); margin-top: 2px; padding-left: 12px; }

  .contact-panel {
    position: absolute; left: 262px; top: 128px; right: 0; bottom: 0;
    background: linear-gradient(180deg, var(--panel-top), var(--panel-bottom));
  }
  .contact-list {
    position: absolute; right: 72px; top: 146px; width: 220px; text-align: right;
    color: var(--text-light); font-size: 10px; line-height: 1.35;
  }
  .contact-list .group { margin-bottom: 12px; }
  .services { list-style: none; }
  .services li::before { content: "• "; }
  .contact-list .phone { font-size: 12px; font-weight: 600; }

  .icon-column { position: absolute; right: 0; bottom: 0; width: 62px; }
  .icon-tile { width: 62px; height: 58px; display: flex; align-items: center; justify-content: center; }
  .icon-tile--services { background: var(--icon-light); }
  .icon-tile--phone { background: var(--icon-mid); }
  .icon-tile--mail { background: var(--icon-dark); }
  .icon-tile svg { width: 20px; height: 20px; fill: none; stroke: #fff; stroke-width: 1.8; }
</style>
</head>
<body>
<div class="canvas">

  <section class="card card--front" aria-label="Card front">
    <div class="band band--top"></div>
    <div class="brand">
      <span class="brand__name">Vorn Electrical</span>
      <span class="brand__suffix">Services PTY LTD</span>
    </div>
    <p class="licence">REC:58104</p>
    <div class="band band--bottom"></div>
  </section>

  <section class="card card--back" aria-label="Card back">
    <div class="brand">
      <span class="brand__name">Vorn Electrical</span>
      <span class="brand__suffix">Services PTY LTD</span>
    </div>

    <div class="contact-panel"></div>

    <div class="name-box">
      <p class="name-box__name">Call Teodor</p>
      <p class="name-box__title">Electrician</p>
    </div>

    <div class="contact-list">
      <ul class="group services">
        <li>Domestic</li>
        <li>Commercial</li>
        <li>Industrial</li>
      </ul>
      <div class="group">
        <p class="phone">0488157093</p>
      </div>
      <div class="group">
        <p>vornelectricalservices@kestramail.com</p>
      </div>
    </div>

    <div class="icon-column">
      <div class="icon-tile icon-tile--services">
        <svg viewBox="0 0 24 24" aria-hidden="true"><path d="M5 12 L10 17 L19 7"/></svg>
      </div>
      <div class="icon-tile icon-tile--phone">
        <svg viewBox="0 0 24 24" aria-hidden="true"><path d="M4 9 C4 6 8 5 12 5 C16 5 20 6 20 9 L17 10 L16 8 H8 L7 10 Z"/><rect x="6" y="12" width="12" height="8" rx="1"/></svg>
      </div>
      <div class="icon-tile icon-tile--mail">
        <svg viewBox="0 0 24 24" aria-hidden="true"><rect x="3" y="6" width="18" height="12"/><path d="M3 6 L12 13 L21 6"/></svg>
      </div>
    </div>
  </section>

</div>
</body>
</html>
```